Storyboard sketches for short, graphic video reel

We would like an art director/designer to sketch out the frames of a short :30 show reel for our agency, Quill. The reel is focused on our digital marketing capabilities.
We have frame-by-frame directions for you to work from with specific ideas, but we are open to any improvements you may suggest.
Updates
Target Market(s)
Other agencies looking to outsource to us, potential clients - in the Asia, English-speaking market
Industry/Entity Type
Digital
Requirements
Must have
- Must include the Quill logo (see attached)

```html
<!DOCTYPE html>
<html lang="en">
<head>
<meta charset="utf-8">
<title>Quill — Show Reel Storyboard</title>
<link href="https://fonts.googleapis.com/css2?family=Ubuntu:wght@500;700&family=Arimo:wght@400;700&display=swap" rel="stylesheet">
<style>
  :root{
    --paper:#ffffff;
    --ink:#1a1a1a;
    --frame:#111111;
    --rule:#b5b5b5;
    --mark:#8f8f8f;
    --mark-light:#d2d2d2;
    --word:#9a9a9a;
    --bar:#000000;
    --bar-text:#ffffff;
    --arrow:#2a8fd0;
    --arrow-light:#9fd2f2;
    --tile:#8d8d8d;
    --tick:#d2232a;
  }
  *{margin:0;padding:0;box-sizing:border-box}
  html,body{width:1200px;height:848px;overflow:hidden;background:var(--paper)}
  .board{position:relative;width:1200px;height:848px;font-family:"Arimo",Arial,sans-serif;color:var(--ink);overflow:hidden}
  .sheet{position:absolute;left:102px;top:38px;width:996px;height:809px;border:3px solid var(--frame)}
  .rule-v{position:absolute;top:40px;width:1px;height:805px;background:var(--rule)}
  .rule-h{position:absolute;left:105px;width:990px;height:1px;background:var(--rule)}
  .bar{position:absolute;background:var(--bar);color:var(--bar-text)}
  .frame-no{position:absolute;left:4px;bottom:0;font:700 34px/1 "Arimo",Arial,sans-serif}
  .caption{position:absolute;left:60px;top:2px;right:8px;font-size:11px;line-height:12px}
  .caption b{font-weight:700}
  .caption .gap{display:block;height:6px}
  .music{position:absolute;left:106px;top:279px;font-size:11px;line-height:12.5px;width:350px}
  .abs{position:absolute;white-space:nowrap}
  .wordmark{font-family:"Ubuntu",Verdana,sans-serif;font-weight:700;color:var(--mark);letter-spacing:-2px;line-height:1}
  .wordmark.light{color:var(--mark-light)}
  .tagline{font-family:"Ubuntu",Verdana,sans-serif;font-weight:700;color:var(--ink)}
  .term{font-family:"Ubuntu",Verdana,sans-serif;font-weight:700;color:var(--word);line-height:1}
  .stack{font-family:"Ubuntu",Verdana,sans-serif;font-weight:700;color:var(--ink);line-height:.95}
  .live{font-family:"Ubuntu",Verdana,sans-serif;font-weight:700;font-style:italic;color:#eeeeee;-webkit-text-stroke:1px #8a8a8a;line-height:1}
  .tile{position:absolute;width:50px;height:50px;border-radius:8px;background:var(--tile)}
  .shot{position:absolute;background:linear-gradient(#e9eef5,#cfd9e6);border:1px solid #c0c0c0}
  .app{position:absolute;width:64px;height:64px}
  .ticker{font:700 10px/1 "Arimo",Arial,sans-serif;color:var(--ink)}
  .contact{font-family:"Ubuntu",Verdana,sans-serif;font-weight:700;color:#b4b4b4;font-size:11px;line-height:14px;text-align:center}
  svg.arrow{position:absolute;overflow:visible}
</style>
</head>
<body>
<div class="board">
  <div class="sheet"></div>
  <div class="rule-v" style="left:458px"></div>
  <div class="rule-v" style="left:778px"></div>
  <div class="rule-h" style="top:317px"></div>
  <div class="rule-h" style="top:573px"></div>

  <svg width="0" height="0" style="position:absolute">
    <defs>
      <linearGradient id="arrowFill" x1="0" y1="0" x2="0" y2="1">
        <stop offset="0" stop-color="var(--arrow-light)"/>
        <stop offset="1" stop-color="var(--arrow)"/>
      </linearGradient>
    </defs>
  </svg>

  <!-- Frame 1: intro -->
  <div class="abs wordmark" style="left:207px;top:66px;font-size:72px">Quill</div>
  <div class="abs tagline" style="left:244px;top:150px;font-size:16px">...We Build It</div>
  <svg class="arrow" style="left:250px;top:178px" width="110" height="22" viewBox="0 0 110 22">
    <path d="M0 11 L18 2 L16 8 Q60 4 108 0 L106 14 Q60 16 16 15 L18 20 Z" fill="url(#arrowFill)" stroke="#333" stroke-width=".6"/>
  </svg>
  <div class="abs term" style="left:363px;top:180px;font-size:17px">Awareness</div>
  <div class="bar" style="left:105px;top:225px;width:353px;height:52px">
    <span class="frame-no">1</span>
    <p class="caption"><b>Intro</b>: fade in Quill logo. Then “We Build It.” Cycle through terms on right: “Awareness. Preference. Sales.”</p>
  </div>
  <p class="music">MUSIC<br>Suggest music begin at logo introduction. Tone is: bright, confident, warm, quick tempo</p>

  <!-- Frame 2: increase -->
  <div class="abs term" style="left:459px;top:58px;font-size:19px">Awareness</div>
  <div class="abs term" style="left:459px;top:108px;font-size:19px">Preference</div>
  <div class="abs term" style="left:459px;top:161px;font-size:19px">Sales</div>
  <svg class="tile" style="left:569px;top:42px" viewBox="0 0 50 50" aria-label="Awareness icon">
    <path d="M12 44 A16 16 0 0 1 44 44 Z" fill="#fff"/>
    <g stroke="#fff" stroke-width="2"><line x1="28" y1="22" x2="28" y2="10"/><line x1="18" y1="25" x2="12" y2="15"/><line x1="38" y1="25" x2="44" y2="15"/></g>
  </svg>
  <svg class="tile" style="left:569px;top:95px" viewBox="0 0 50 50" aria-label="Preference checklist icon">
    <g fill="#fff"><rect x="8" y="7" width="10" height="10"/><rect x="8" y="20" width="10" height="10"/><rect x="8" y="33" width="10" height="10"/></g>
    <path d="M21 24 L26 30 L40 14" fill="none" stroke="var(--tick)" stroke-width="3"/>
  </svg>
  <div class="tile" style="left:569px;top:147px;background:linear-gradient(#9a9a9a,#7f7f7f)" role="img" aria-label="Handshake illustration for sales"></div>
  <svg class="arrow" style="left:620px;top:58px" width="130" height="110" viewBox="0 0 130 110">
    <g fill="url(#arrowFill)" stroke="#333" stroke-width=".6">
      <path d="M0 12 L18 0 L17 7 Q80 6 126 30 L122 42 Q80 20 17 19 L18 26 Z"/>
      <path d="M0 58 L18 46 L17 53 Q80 52 126 66 L122 78 Q80 64 17 65 L18 72 Z"/>
      <path d="M0 90 L18 78 L17 85 Q80 76 126 70 L124 84 Q80 92 17 97 L18 104 Z"/>
    </g>
  </svg>
  <div class="abs wordmark" style="right:426px;top:158px;font-size:50px">Quill</div>
  <div class="bar" style="left:458px;top:225px;width:320px;height:52px">
    <span class="frame-no">2</span>
    <p class="caption"><b>Increase</b>: Quill logo moves to bottom right, “Awareness, Preference, and Sales” left align and complementary graphics animate in moving from low to high points.</p>
  </div>

  <!-- Frame 3: business outcomes -->
  <div class="abs stack" style="left:782px;top:42px;font-size:36px;text-align:center;width:100px">We<br>Build<br>It</div>
  <svg class="arrow" style="left:795px;top:70px" width="70" height="140" viewBox="0 0 70 140">
    <g fill="url(#arrowFill)" stroke="#333" stroke-width=".6">
      <path d="M12 0 L22 14 L16 14 Q10 70 22 135 L12 135 Q2 70 9 14 L3 14 Z"/>
      <path d="M32 80 L42 92 L37 92 Q34 112 40 135 L31 135 Q27 112 30 92 L24 92 Z"/>
      <path d="M52 80 L62 92 L57 92 Q58 112 66 135 L57 135 Q49 112 50 92 L44 92 Z"/>
    </g>
  </svg>
  <div class="abs wordmark" style="right:115px;top:158px;font-size:50px">Quill</div>
  <div class="bar" style="left:778px;top:225px;width:317px;height:52px">
    <span class="frame-no">3</span>
    <p class="caption"><b>Business outcomes:</b> replace terms with “We Build It” in a vertical build.</p>
  </div>

  <!-- Frame 4: services -->
  <div class="abs stack" style="left:104px;top:316px;font-size:36px;text-align:center;width:100px">We<br>Build<br>It</div>
  <div class="abs term" style="left:221px;top:360px;font-size:38px">Websites</div>
  <div class="abs wordmark" style="right:793px;top:424px;font-size:52px">Quill</div>
  <div class="bar" style="left:105px;top:488px;width:353px;height:48px">
    <span class="frame-no">4</span>
    <p class="caption"><b>Services</b>: We Build It remains. And new terms cycle through: “Websites. Apps. Databases.”</p>
  </div>

  <!-- Frame 5: websites -->
  <div class="abs term" style="left:486px;top:314px;font-size:34px">Websites</div>
  <div class="abs live" style="left:680px;top:318px;font-size:30px">live</div>
  <div class="shot" style="left:495px;top:362px;width:62px;height:60px" role="img" aria-label="Live screen of a client website"></div>
  <div class="shot" style="left:573px;top:362px;width:62px;height:60px;background:linear-gradient(#dfe8d6,#b9c8a8)" role="img" aria-label="Live screen of a client website"></div>
  <div class="shot" style="left:645px;top:362px;width:66px;height:60px" role="img" aria-label="Live screen of a client website"></div>
  <svg class="arrow" style="left:620px;top:372px" width="110" height="40" viewBox="0 0 110 40">
    <path d="M0 14 L18 2 L17 9 Q70 0 104 24 L98 34 Q70 16 17 21 L18 28 Z" fill="url(#arrowFill)" stroke="#333" stroke-width=".6"/>
  </svg>
  <div class="abs wordmark" style="right:460px;top:440px;font-size:46px">Quill</div>
  <div class="bar" style="left:458px;top:488px;width:320px;height:48px">
    <span class="frame-no">5</span>
    <p class="caption"><b>Websites</b>: “Websites” moves top left, fade in “live” (active) screens of three websites.</p>
  </div>

  <!-- Frame 6: apps -->
  <div class="abs term" style="left:835px;top:314px;font-size:34px">Apps</div>
  <div class="abs live" style="left:992px;top:318px;font-size:30px">live</div>
  <div class="app" style="left:810px;top:362px;border-radius:50%;background:radial-gradient(#b9d6f0,#4f7fb0)" role="img" aria-label="App icon of a live app"></div>
  <div class="app" style="left:878px;top:366px;border-radius:6px;background:linear-gradient(#7fa8d6,#3d6ea6)" role="img" aria-label="App icon of a live app"></div>
  <div class="app" style="left:946px;top:362px;border-radius:6px;background:radial-gradient(#d8e86a,#3f7a2e)" role="img" aria-label="App icon of a live app"></div>
  <svg class="arrow" style="left:925px;top:372px" width="110" height="40" viewBox="0 0 110 40">
    <path d="M0 14 L18 2 L17 9 Q70 0 104 24 L98 34 Q70 16 17 21 L18 28 Z" fill="url(#arrowFill)" stroke="#333" stroke-width=".6"/>
  </svg>
  <div class="abs wordmark" style="right:150px;top:440px;font-size:46px">Quill</div>
  <div class="bar" style="left:778px;top:488px;width:317px;height:48px">
    <span class="frame-no">6</span>
    <p class="caption"><b>Apps</b>: “Apps” replaces Websites, fade in “live” (active) screens of three apps.</p>
  </div>

  <!-- Frame 7: databases -->
  <div class="abs term" style="left:163px;top:574px;font-size:28px">Databases</div>
  <div class="abs live" style="left:334px;top:576px;font-size:28px">live</div>
  <div class="shot" style="left:214px;top:612px;width:92px;height:46px;background:repeating-linear-gradient(#f4f6f9 0 4px,#dde4ee 4px 5px)" role="img" aria-label="Database table screen"></div>
  <svg class="arrow" style="left:292px;top:620px" width="110" height="40" viewBox="0 0 110 40">
    <path d="M0 20 L18 8 L17 15 Q70 4 108 12 L106 26 Q70 20 17 27 L18 34 Z" fill="url(#arrowFill)" stroke="#333" stroke-width=".6"/>
  </svg>
  <svg class="arrow" style="left:166px;top:664px" width="28" height="10" viewBox="0 0 28 10">
    <path d="M0 5 L8 0 L7 3 L28 3 L28 7 L7 7 L8 10 Z" fill="url(#arrowFill)" stroke="#333" stroke-width=".4"/>
  </svg>
  <div class="abs ticker" style="left:198px;top:665px">March&nbsp;&nbsp;12,320&nbsp;&nbsp;April 15,974&nbsp;&nbsp;May 18,786&nbsp;&nbsp;Ju</div>
  <div class="abs wordmark" style="right:810px;top:692px;font-size:44px">Quill</div>
  <div class="bar" style="left:164px;top:757px;width:294px;height:48px"></div>
  <div class="bar" style="left:105px;top:768px;width:353px;height:37px">
    <span class="frame-no">7</span>
  </div>
  <p class="caption" style="left:164px;top:758px;width:292px;color:var(--bar-text)"><b>Databases</b>: “Databases” replaces Apps, build in database graphic with accompanying endless scroll of sample data, plus three client logos (clients we’ve built databases for)</p>

  <!-- Frame 8: end -->
  <div class="abs wordmark light" style="left:520px;top:590px;font-size:84px">Quill</div>
  <div class="abs tagline" style="left:567px;top:680px;font-size:20px">...We Build It</div>
  <div class="bar" style="left:458px;top:757px;width:320px;height:48px">
    <span class="frame-no">8</span>
    <p class="caption"><b>End</b>: Goes from fade to black to fade in Quill logo. End with same placement as intro: Quill logo and “We Build It.”</p>
  </div>

  <!-- Frame 9: contact -->
  <div class="abs wordmark" style="left:840px;top:592px;font-size:84px">Quill</div>
  <div class="abs tagline" style="left:885px;top:682px;font-size:19px">...We Build It</div>
  <div class="abs contact" style="left:878px;top:707px;width:140px">Dana Whitlock<br>481 20736<br>E: dwhitlock@quill.uk.com</div>
  <div class="bar" style="left:778px;top:757px;width:317px;height:48px">
    <span class="frame-no">9</span>
    <p class="caption"><b>Contact</b>: Fade in contact info at right of “Quill. We Build It.”<span class="gap"></span>Dana Whitlock contact info?</p>
  </div>
</div>
</body>
</html>
```